Dorian Blakely & Morning Lanterns

I need a cd cover designed for a Gospel/Christian Choir. I'm attaching the main picture I want on the cover. This is our single "Lift my heart higher".

Requirements
Must have
• Single name: Lift My Heart Higher

```html
<!DOCTYPE html>
<html lang="en">
<head>
<meta charset="utf-8">
<title>Lift My Heart Higher – Dorian Blakely &amp; Morning Lanterns</title>
<link rel="stylesheet" href="https://fonts.googleapis.com/css2?family=Anton&family=Montserrat:wght@600&display=swap">
<style>
  :root {
    --frame: #050505;
    --ink-dark: #1a0f05;
    --amber: #e98a2a;
    --amber-deep: #7a3a10;
    --night: #1b120c;
    --gold-light: #fff6b0;
    --gold: #f5c63a;
    --gold-deep: #c98a12;
    --web-white: #f4efe6;
  }
  html, body {
    margin: 0;
    padding: 0;
    width: 1200px;
    height: 1200px;
    overflow: hidden;
    background: var(--frame);
  }
  .cover {
    position: relative;
    width: 1200px;
    height: 1200px;
    background: var(--frame);
  }
  .cover-photo {
    position: absolute;
    left: 30px;
    top: 30px;
    width: 1140px;
    height: 1140px;
    background:
      radial-gradient(circle at 14% 10%, rgba(255,226,160,0.95) 0, rgba(255,170,70,0.55) 9%, rgba(0,0,0,0) 20%),
      radial-gradient(ellipse at 62% 22%, rgba(233,138,42,0.9) 0, rgba(122,58,16,0.6) 40%, rgba(0,0,0,0) 70%),
      linear-gradient(100deg, var(--night) 0%, #3a2414 35%, var(--amber-deep) 65%, #4a2a16 100%);
  }
  .website {
    position: absolute;
    top: 44px;
    left: 0;
    width: 1200px;
    text-align: center;
    font-family: "Montserrat", sans-serif;
    font-weight: 600;
    font-size: 19px;
    letter-spacing: 9px;
    color: var(--web-white);
  }
  .single-title {
    position: absolute;
    left: 96px;
    right: 96px;
    top: 660px;
    margin: 0;
    font-family: "Anton", sans-serif;
    font-weight: 400;
    font-size: 152px;
    line-height: 1;
  }
  .title-line {
    display: flex;
    justify-content: space-between;
    height: 168px;
  }
  .title-line.centered {
    justify-content: center;
    gap: 60px;
  }
  .title-line span {
    background:
      repeating-linear-gradient(135deg, rgba(255,255,255,0.35) 0 3px, rgba(0,0,0,0) 3px 7px),
      linear-gradient(180deg, var(--gold-light) 0%, var(--gold) 45%, var(--gold-deep) 100%);
    -webkit-background-clip: text;
    background-clip: text;
    color: transparent;
    filter: drop-shadow(3px 5px 0 var(--ink-dark)) drop-shadow(0 0 10px rgba(0,0,0,0.6));
  }
  .gap { width: 80px; }
</style>
</head>
<body>
  <main class="cover">
    <div class="cover-photo" role="img" aria-label="Portrait of the artist in a dark satin suit leaning against a warmly lit brick wall beside a glowing street lamp at night"></div>
    <div class="website">WWW.lanternsongs.COM</div>
    <h1 class="single-title" aria-label="Lift My Heart Higher">
      <div class="title-line"><span>L</span><span>I</span><span>F</span><span>T</span><span class="gap"></span><span>M</span><span>Y</span></div>
      <div class="title-line centered"><span>H</span><span>E</span><span>A</span><span>R</span><span>T</span></div>
      <div class="title-line"><span>H</span><span>I</span><span>G</span><span>H</span><span>E</span><span>R</span></div>
    </h1>
  </main>
</body>
</html>
```